- Please see our description here:
http://zestova.example/lorin/blog/zestova-player-v1

- Zestova Player needs to "look & feel" like a HTML 5 Web application.

- All of the additional pages and Zestova elements that the user goes to, need to fit within the player interface. So for example, when the user clicks on the profile it will pull it into the player as apposed to opening a new page.

- For further instructions, please send me a private message to http://zestova.example/lorin and we will send you our site work flow chart interface examples.

I just added 2 mockups that I want you guys to look at carefully and understand what we are trying to do:

http://zestova.example/media/files/public/blog/image-4-1564_2.jpg
http://zestova.example/media/files/public/blog/image-4-1564_4.jpg

the idea is that everything is controlled from the new menu button (the nice purple one).
it will throw an overlay with all our navigational choices.
and those icons will be displayed.
with this approach, we can get to everywhere in our site with no more then 2 clicks.
right from the zestova player.
if the users profile pic is clicked, we pull in the profile in an overlay as well.
we almost never leave the player.

can we do it or what?

Lorin

Target Market(s)

Social Foodies, Food Lovers, Pro and Amateur Chefs, House wives and husbands, Recipe lovers, and more

Industry/Entity Type

Media

Requirements
Must have
• We are staying on the same page as user selects options from the menu. Must have an application feel.

Try logging in to our current site and look around, to see partial example of what we are talking about. (www.zestova.example)

The site should feature a friendly chef, a character that offers pop-up tips on how to use features of the site.

In the top right corner of the site we need a common menu that takes user to a dashboard popup from which she can do most common activities on the site (create, share, search, suggest, compete, my profile)

```html
<!DOCTYPE html>
<html lang="en">
<head>
<meta charset="utf-8">
<title>Zestova Player</title>
<link rel="stylesheet" href="https://fonts.googleapis.com/css2?family=Varela+Round&family=Arimo:wght@400;700&display=swap">
<style>
  :root {
    --page: #ffffff;
    --shell: #343434;
    --stage: #474747;
    --stage-edge: #5a5a5a;
    --bar: #0b0b0b;
    --orange: #ff7a12;
    --orange-deep: #f05a00;
    --purple: #8a5ce6;
    --menu-grey: #5b5b5b;
    --comments-bg: #1c1c1c;
    --rule: #c9600f;
    --white: #ffffff;
    --text-soft: #e0a070;
  }
  * { box-sizing: border-box; margin: 0; padding: 0; }
  html, body { width: 900px; height: 1200px; overflow: hidden; background: var(--page); }
  body { position: relative; font-family: "Varela Round", "Arimo", sans-serif; }
  .abs { position: absolute; }

  .shell { left: 126px; top: 166px; width: 648px; height: 744px; background: var(--shell); }

  .share-row { display: flex; gap: 5px; }
  .share-row span { width: 22px; height: 22px; border-radius: 4px; background: linear-gradient(var(--orange), var(--orange-deep)); }
  .site-share { left: 646px; top: 181px; }

  .brand { right: 148px; top: 232px; font-size: 58px; color: var(--orange); letter-spacing: -1px; line-height: 1; }
  .header-rule { left: 150px; top: 297px; width: 600px; height: 1px; background: #9a9a9a; }

  .stage { left: 150px; top: 311px; width: 600px; height: 384px; border-radius: 14px; background: var(--stage); box-shadow: inset 0 0 0 2px var(--stage-edge), 0 3px 4px rgba(0,0,0,.5); }
  .title-bar { left: 162px; top: 322px; width: 576px; height: 36px; background: var(--bar); border-radius: 3px; }
  .dish-title { right: 174px; top: 328px; color: var(--white); font-size: 19px; }

  .thumb { left: 162px; width: 92px; border-radius: 2px; }
  .see-more { left: 162px; top: 676px; font-family: "Arimo", sans-serif; font-size: 7px; color: var(--orange); }

  .hero { left: 258px; top: 364px; width: 480px; height: 320px; background: radial-gradient(ellipse at 60% 55%, #b27a55 0%, #c79d7a 35%, #d9c2a6 60%, #c08a4c 100%); }
  .next-btn { left: 712px; top: 491px; }

  .controls { left: 262px; top: 654px; width: 472px; height: 22px; background: rgba(10,10,10,.85); border-radius: 2px; }
  .count-box { left: 288px; top: 658px; width: 66px; height: 13px; background: var(--white); font-family: "Arimo", sans-serif; font-size: 7px; color: #111; padding: 2px 3px; }
  .yums { left: 360px; top: 656px; display: flex; align-items: center; gap: 3px; color: var(--white); font-size: 11px; }
  .stars { left: 454px; top: 655px; }
  .recipe-btn { left: 564px; top: 658px; width: 96px; height: 13px; border-radius: 7px; background: var(--orange-deep); color: var(--white); font-family: "Arimo", sans-serif; font-size: 8px; text-align: center; line-height: 13px; }
  .player-share { left: 669px; top: 659px; gap: 3px; }
  .player-share span { width: 12px; height: 12px; border-radius: 2px; }

  .menu-tab { left: 174px; top: 324px; width: 132px; height: 32px; border-radius: 5px 5px 0 0; background: linear-gradient(#a57cf5, var(--purple)); color: var(--orange); font-size: 18px; text-align: center; line-height: 32px; }
  .menu-panel { left: 174px; top: 356px; width: 132px; height: 182px; background: var(--menu-grey); box-shadow: 2px 3px 6px rgba(0,0,0,.55); }
  .avatar { left: 186px; top: 371px; width: 108px; height: 72px; background: linear-gradient(#4a4a4a, #3a3a3a); border: 2px solid #222; }
  .member-name { left: 186px; top: 452px; color: var(--white); font-size: 14px; word-spacing: 3px; }
  .menu-btn { left: 186px; width: 108px; height: 24px; background: #2a2a2a; border: 1px solid #777; display: flex; align-items: center; justify-content: space-between; padding: 0 7px 0 4px; font-size: 12px; }
  .menu-btn.message { top: 473px; color: var(--orange); }
  .menu-btn.add-friend { top: 503px; color: #ffd21a; }

  .comments { left: 150px; top: 707px; width: 600px; height: 185px; background: var(--comments-bg); }
  .comments-title { left: 156px; top: 715px; color: var(--orange); font-size: 16px; }
  .comment-rule { left: 156px; width: 588px; height: 1px; background: var(--rule); }
  .comment-line { left: 156px; font-family: "Arimo", sans-serif; font-size: 7.4px; color: var(--text-soft); white-space: nowrap; }
  .comment-input { left: 156px; top: 826px; width: 588px; height: 42px; background: var(--white); border: none; }
  .post-btn { left: 684px; top: 874px; width: 60px; height: 14px; border-radius: 7px; background: #3a3a3a; border: 1px solid #666; color: var(--orange); font-family: "Arimo", sans-serif; font-size: 8px; text-align: center; line-height: 12px; }
</style>
</head>
<body>
  <div class="abs shell"></div>

  <div class="abs share-row site-share"><span></span><span></span><span></span><span></span></div>
  <div class="abs brand">Zestova</div>
  <div class="abs header-rule"></div>

  <div class="abs stage"></div>
  <div class="abs title-bar"></div>
  <div class="abs dish-title">Shawarma Pita and Fries</div>

  <div class="abs thumb" style="top:364px;height:72px;background:linear-gradient(#c9a27a,#8e6a4a)" role="img" aria-label="Thumbnail of a dish"></div>
  <div class="abs thumb" style="top:442px;height:72px;background:linear-gradient(#c7905a,#7a5535)" role="img" aria-label="Thumbnail of a dish"></div>
  <div class="abs thumb" style="top:520px;height:68px;background:linear-gradient(#d2a04e,#7b5220)" role="img" aria-label="Thumbnail of roasted potatoes"></div>
  <div class="abs thumb" style="top:596px;height:68px;background:linear-gradient(#8a6a7a,#b07aa8)" role="img" aria-label="Thumbnail of a berry drink"></div>
  <div class="abs see-more">See More</div>

  <div class="abs hero" role="img" aria-label="Photo of a shawarma pita with meat, tomato and fries"></div>
  <svg class="abs next-btn" width="24" height="24" viewBox="0 0 24 24"><circle cx="12" cy="12" r="11" fill="#2b2b2b" stroke="#888" stroke-width="1"/><polygon points="9,6 18,12 9,18" fill="#ddd"/></svg>

  <div class="abs controls"></div>
  <svg class="abs" style="left:268px;top:658px" width="14" height="14" viewBox="0 0 14 14"><rect x="1" y="1" width="4" height="12" fill="#fff"/><rect x="8" y="1" width="4" height="12" fill="#fff"/></svg>
  <div class="abs count-box">1,000,000 people</div>
  <div class="abs yums"><svg width="10" height="12" viewBox="0 0 10 12"><rect x="0" y="6" width="4" height="6" fill="#ff7a12"/><rect x="5" y="1" width="4" height="11" fill="#ff7a12"/></svg>Yums</div>
  <svg class="abs stars" width="102" height="18" viewBox="0 0 102 18">
    <defs><polygon id="star" points="9,0 11.2,6.2 18,6.4 12.6,10.4 14.6,17 9,13.1 3.4,17 5.4,10.4 0,6.4 6.8,6.2"/></defs>
    <g fill="#f07a18">
      <use href="#star" x="0"/><use href="#star" x="21"/><use href="#star" x="42"/><use href="#star" x="63"/><use href="#star" x="84"/>
    </g>
  </svg>
  <div class="abs recipe-btn">View Recipe</div>
  <div class="abs share-row player-share"><span></span><span></span><span></span><span></span></div>

  <div class="abs menu-tab">Menu</div>
  <div class="abs menu-panel"></div>
  <div class="abs avatar" role="img" aria-label="Member profile picture placeholder"></div>
  <div class="abs member-name">Marlo Finch</div>
  <div class="abs menu-btn message">
    <svg width="26" height="18" viewBox="0 0 26 18"><rect x="1" y="1" width="24" height="16" fill="#fff"/><polyline points="1,1 13,10 25,1" fill="none" stroke="#2a2a2a" stroke-width="2"/></svg>
    <span>Message</span>
  </div>
  <div class="abs menu-btn add-friend">
    <svg width="18" height="18" viewBox="0 0 18 18"><rect x="6.5" y="1" width="5" height="16" fill="#fff"/><rect x="1" y="6.5" width="16" height="5" fill="#fff"/></svg>
    <span>Add Friend</span>
  </div>

  <div class="abs comments"></div>
  <div class="abs comments-title">Comments</div>
  <div class="abs comment-rule" style="top:736px"></div>
  <div class="abs comment-line" style="top:741px">Lorem ipsum dolor sit amet, consectetur adipisicing elit, sed do eiusmod tempor incididunt ut labore et dolore magna aliqua.</div>
  <div class="abs comment-line" style="top:754px">Lorem ipsum dolor sit amet, consectetur adipisicing elit, sed do eiusmod tempor incididunt ut labore et dolore magna aliqua.</div>
  <div class="abs comment-rule" style="top:772px"></div>
  <div class="abs comment-line" style="top:778px">Lorem ipsum dolor sit amet, consectetur adipisicing elit, sed do eiusmod tempor incididunt ut labore et dolore magna aliqua.</div>
  <div class="abs comment-line" style="top:790px">Lorem ipsum dolor sit amet, consectetur adipisicing elit, sed do eiusmod tempor incididunt ut labore et dolore magna aliqua.</div>
  <div class="abs comment-rule" style="top:808px"></div>
  <div class="abs comment-input"></div>
  <div class="abs post-btn">Post Comment</div>
</body>
</html>
```